Side of Page Partnership-type Letterhead Design for Chiropractic Office

Side oriented letterhead with practice locations/demographics, physician names and company logo

Target Market(s)

Healthcare Professionals & Attorneys

Industry/Entity Type

Healthcare

Font styles to use
Other font styles liked:
• Font of Logo is Trajan Pro, but not a deal breaker if we try something else

Colors

Designer to choose colors to be used in the design.

Requirements
Must have
• All info from attached documents

```html
<!DOCTYPE html>
<html lang="en">
<head>
<meta charset="utf-8">
<title>Keystone Chiropractic Letterhead</title>
<link rel="stylesheet" href="https://fonts.googleapis.com/css2?family=Cinzel:wght@400;600&family=Montserrat:wght@400;500&display=swap">
<style>
  :root {
    --backdrop: #3d82c4;
    --paper: #ffffff;
    --ink: #4a4a4a;
    --ink-soft: #6d6d6d;
    --brand: #3a3a3a;
    --accent: #f0a43a;
    --mark-dot: #7fae4a;
    --signature: #1f3fb0;
    --watermark: #efefef;
  }
  * { margin: 0; padding: 0; box-sizing: border-box; }
  html, body { width: 1200px; height: 900px; overflow: hidden; }
  body {
    background: var(--backdrop);
    font-family: "Montserrat", Arial, sans-serif;
    color: var(--ink);
  }
  .letterhead {
    position: absolute;
    left: 275px; top: 30px;
    width: 650px; height: 840px;
    background: var(--paper);
    box-shadow: 0 10px 30px rgba(0,0,0,0.25);
    overflow: hidden;
  }
  .brand {
    position: absolute;
    right: 48px; top: 48px;
    display: flex; align-items: center; gap: 10px;
  }
  .brand-name {
    font-family: "Cinzel", Georgia, serif;
    font-weight: 600;
    font-size: 22px;
    letter-spacing: 1px;
    color: var(--brand);
  }
  .brand-dot {
    width: 18px; height: 18px; border-radius: 50%;
    background: var(--mark-dot);
  }
  .sidebar {
    position: absolute;
    left: 48px; top: 140px;
    width: 132px;
  }
  .physicians { list-style: none; margin-bottom: 28px; }
  .physicians li {
    font-family: "Cinzel", Georgia, serif;
    font-size: 9px;
    line-height: 1.65;
    color: var(--brand);
    font-weight: 600;
    white-space: nowrap;
  }
  .physicians .credential { font-weight: 400; color: var(--ink-soft); }
  .location { margin-bottom: 22px; font-size: 8px; line-height: 1.55; color: var(--ink-soft); }
  .location h3 {
    font-family: "Cinzel", Georgia, serif;
    font-size: 9px; font-weight: 600;
    color: var(--brand);
    margin-bottom: 2px;
  }
  .divider {
    position: absolute;
    left: 192px; top: 140px;
    width: 1.5px; height: 470px;
    background: var(--accent);
  }
  .letter-body {
    position: absolute;
    left: 214px; top: 140px;
    width: 388px;
    font-size: 10.5px;
    line-height: 1.55;
  }
  .letter-body p { margin-bottom: 14px; text-align: justify; }
  .sign-off { position: absolute; left: 214px; top: 560px; }
  .signature {
    display: block;
    width: 120px; height: 26px;
    background: linear-gradient(90deg, rgba(31,63,176,0.18), rgba(31,63,176,0.06));
    border-radius: 3px;
    margin-bottom: 4px;
  }
  .signer-title { font-size: 10px; color: var(--ink); }
  .backdrop-mark {
    position: absolute;
    left: 110px; top: 630px;
    width: 540px; height: 210px;
    background: radial-gradient(ellipse at 55% 70%, var(--watermark) 0%, rgba(239,239,239,0.6) 50%, rgba(239,239,239,0) 80%);
  }
</style>
</head>
<body>
  <main class="letterhead">
    <header class="brand">
      <span class="brand-name">Keystone Chiropractic</span>
      <span class="brand-dot"></span>
    </header>

    <aside class="sidebar">
      <ul class="physicians">
        <li>Owen Harlow, <span class="credential">DC, DACNB</span></li>
        <li>Neil Harlow, <span class="credential">DC</span></li>
        <li>Evan Brandt, <span class="credential">DC</span></li>
        <li>Paul Kessler, <span class="credential">DC</span></li>
        <li>Reid Calloway, <span class="credential">DC</span></li>
        <li>Mark Ellison, <span class="credential">DC</span></li>
      </ul>
      <div class="location">
        <h3>Fairbrook</h3>
        <p>2180 N. Alder St<br>Fairbrook, ST 10211<br>p 555 555 0142</p>
      </div>
      <div class="location">
        <h3>Linden Falls</h3>
        <p>415 E. Maple Ave<br>Linden Falls, ST 10281<br>p 555 555 0178</p>
      </div>
      <div class="location">
        <h3>Ashgrove</h3>
        <p>96 Birchwood Rd<br>Ashgrove, ST 10230<br>p 555 555 0193</p>
      </div>
    </aside>

    <div class="divider"></div>

    <section class="letter-body">
      <p>Letterhead samples are a great way of deciding what kind of letterhead you want to design for you and your company. The internet has a ton of great letterhead samples to browse through. Whether you want something simple, with just a couple lines of text, or your business name, information, and logo stunning, with photos and artwork, there are samples online for basically any type of letterhead you could want.</p>
      <p>Any business could easily benefit from browsing through some letterhead samples. It's great to get an idea for what kind of letterhead your company might want. Letterheads are one of the tools that a business can use to help increase their customer base. A letter to a client is quite effective, and a simple yet well known idea. It is often unlikely that a customer will forget about you when you remember them, so make some letterhead samples of your own today.</p>
      <p>Whether you want to get new customers to remember you and reminders of your company, or you just want to send out friendly letters to clients, try out some letterhead samples and customizing your own letterhead. You will not regret it, and I'm sure you will add a new tool to your business arsenal of networking, marketing and advertising tools.</p>
    </section>

    <div class="sign-off">
      <span class="signature" role="img" aria-label="Handwritten signature of Daniel Whitmore"></span>
      <p class="signer-title">company director</p>
    </div>

    <div class="backdrop-mark" role="img" aria-label="Faint oversized practice emblem decoration"></div>
  </main>
</body>
</html>
```